Cover for a recovery from breast augmentation surgery pamphlet

Need a cover which includes my logo for new pamphlet on recovering from breast augmentation surgery It is just a quick how to guide.
I would like the cover to incorporate the Borela logo(2 options given) and be simple and clean. Will require in a vector file as well.

The title:
Well, Your Chest Is Upgraded...
WHAT NEXT?!

By: Borela

A little about me: I am an adult industry writer and am looking to do a mainstream project. This is a project I want to appeal to mainstream women.

Target Market(s)

Women who are recovering from or entertaining breast augmentation surgery

Font styles to use
Serif

Requirements
Must have
• One Borela logo, titile, and by Borela
Nice to have
• i love modern clean sleek design that is easy to read
Should not have
• nothing that would offend women or make them uncomfortable about their body

```html
<!DOCTYPE html>
<html lang="en">
<head>
<meta charset="utf-8">
<title>Borela – Recovery Guide Cover</title>
<link href="https://fonts.googleapis.com/css2?family=Cormorant+Garamond:wght@500&family=Open+Sans:wght@400&display=swap" rel="stylesheet">
<style>
  :root {
    --magenta: #c9318d;
    --pink-mid: #e066a8;
    --pink-light: #f09ac6;
    --skin-light: #f3d6c6;
    --skin-mid: #e6b9a0;
    --skin-shadow: #d7a58a;
    --paper: #ffffff;
    --text-light: #ffffff;
  }
  * { margin: 0; padding: 0; box-sizing: border-box; }
  html, body { width: 897px; height: 1200px; overflow: hidden; background: var(--paper); }
  .cover {
    position: relative;
    width: 897px;
    height: 1200px;
    background: var(--paper);
    overflow: hidden;
    font-family: "Cormorant Garamond", "Times New Roman", serif;
  }
  .cover-art { position: absolute; inset: 0; width: 897px; height: 1200px; }
  .brand {
    position: absolute;
    display: flex;
    align-items: center;
    gap: 10px;
    font-family: "Cormorant Garamond", "Times New Roman", serif;
    font-weight: 500;
  }
  .brand-mark { border-radius: 50%; flex: none; }
  .brand--top { left: 630px; top: 122px; color: var(--magenta); font-size: 50px; }
  .brand--top .brand-mark { width: 18px; height: 18px; background: var(--magenta); }
  .brand--footer { left: 84px; top: 1030px; color: var(--text-light); font-size: 38px; }
  .brand--footer .brand-mark { width: 14px; height: 14px; background: var(--text-light); }
  .title {
    position: absolute;
    left: 360px;
    top: 330px;
    width: 530px;
    text-align: center;
    color: var(--magenta);
    font-weight: 500;
    line-height: 1;
  }
  .title-lead { display: block; font-size: 44px; margin-bottom: 18px; }
  .title-main { display: block; font-size: 62px; letter-spacing: 1px; margin-bottom: 22px; }
  .title-punch { display: block; font-size: 96px; line-height: 0.98; }
  .footer-divider {
    position: absolute;
    left: 250px;
    top: 994px;
    width: 1px;
    height: 120px;
    background: var(--text-light);
  }
  .footer-copy {
    position: absolute;
    left: 291px;
    top: 990px;
    width: 541px;
    color: var(--text-light);
    font-family: "Open Sans", Arial, sans-serif;
    font-size: 11.6px;
    line-height: 20.8px;
    text-align: justify;
  }
</style>
</head>
<body>
<main class="cover">
  <svg class="cover-art" viewBox="0 0 897 1200" aria-hidden="false">
    <defs>
      <linearGradient id="skinTone" x1="0" y1="0" x2="1" y2="1">
        <stop offset="0" stop-color="var(--skin-light)"/>
        <stop offset="0.6" stop-color="var(--skin-mid)"/>
        <stop offset="1" stop-color="var(--skin-shadow)"/>
      </linearGradient>
    </defs>
    <path role="img" aria-label="Photograph of a woman's torso, arm raised, modestly covering her chest with her hand"
          fill="url(#skinTone)"
          d="M0,0 L492,0 C472,150 390,260 355,380 C332,500 334,620 352,700 C382,780 432,830 462,884 L0,884 Z"/>
    <path fill="var(--pink-light)" d="M0,888 C300,884 640,840 897,762 L897,1200 L0,1200 Z"/>
    <path fill="var(--pink-mid)" d="M0,886 C320,880 660,846 897,790 L897,1200 L0,1200 Z"/>
    <path fill="var(--magenta)" d="M0,852 C200,900 600,880 897,818 L897,1200 L0,1200 Z"/>
  </svg>

  <div class="brand brand--top"><span class="brand-mark"></span><span class="brand-name">Borela</span></div>

  <h1 class="title">
    <span class="title-lead">Well, Your Chest Is</span>
    <span class="title-main">UPGRADED...</span>
    <span class="title-punch">WHAT<br>NEXT?!</span>
  </h1>

  <div class="brand brand--footer"><span class="brand-mark"></span><span class="brand-name">Borela</span></div>
  <div class="footer-divider"></div>
  <p class="footer-copy">Health is wealth and after breast augmentation surgery is definitely a time when you need the healthiest food. Stock your cupboards, pantry, refrigerator, and freezer with healthy food and staples. Meal replacement bars and/or shakes with protein powder are great for days where you need to rest rather than prepare food. Never would you guess how difficult grocery shopping and food prep can be when you cannot move your arms or carry more than a gallon of milk. Small amounts of produce are manageable to shop and carry after about a week post-surgery.</p>
</main>
</body>
</html>
```